Luxury Face Oil Label

I'm looking for a simple and sophisticated design for a natural face oil that will target the luxe market. It is a pure Natural product. I have attached the logo, Velumi Organics.

Here's the Copy

LUXE FACIAL OIL

Regenerate. Hydrate. Glow

100% Natural

30ml (1.01 oz)

A complex blend of Pure Oils including Marula, Sea Buckthorn, Rosehip, Neroli, Evening primrose, Argan, Calendula, Lavender, Jojoba, Grapeseed, Baobab, Moringa and Vitamin E oil.

Produced by
Brasso Kettle Ltd
P.O box 7925-00300
Nairobi, Kenya
www.velumiorganics.example

Target Market(s)

High end

Requirements
Must have
• Simple, Please consider the bottle, which is a 30ml clear glass bottle with a gold and white pump. Image attached.
Nice to have
• Very clean designs, not too much going on.
Should not have
• Leaves and nuts.

```html
<!DOCTYPE html>
<html lang="en">
<head>
<meta charset="utf-8">
<title>Velumi Organics – Luxe Facial Oil Label</title>
<link rel="stylesheet" href="https://fonts.googleapis.com/css2?family=Nunito+Sans:wght@300;400&display=swap">
<style>
  :root {
    --backdrop: #f5f5f7;
    --paper: #ffffff;
    --paper-shade: #eceeee;
    --ink-olive: #5e5f4f;
    --frame-sage: #c9c9ae;
    --gold-light: #fdf7a6;
    --gold-warm: #e6b95a;
    --gold-deep: #6b4423;
    --gold-mid: #8f6432;
    --gold-base: #b08a3e;
    --text-on-gold: #ffffff;
  }
  * { margin: 0; padding: 0; box-sizing: border-box; }
  html, body {
    width: 1200px; height: 1060px; overflow: hidden;
    background: var(--backdrop);
    font-family: "Nunito Sans", "Helvetica Neue", sans-serif;
    font-weight: 300;
  }
  .canvas { position: relative; width: 1200px; height: 1060px; }

  .gold {
    background: linear-gradient(90deg,
      var(--gold-light) 0%, var(--gold-warm) 28%, var(--gold-deep) 50%,
      var(--gold-mid) 62%, var(--gold-base) 78%, var(--gold-base) 100%);
  }

  /* Bottle label, flattened */
  .bottle-label {
    position: absolute; left: 130px; top: 250px; width: 440px; height: 580px;
    background: linear-gradient(90deg, var(--paper-shade) 0%, var(--paper) 25%, var(--paper) 70%, var(--paper-shade) 100%);
    box-shadow: 0 2px 10px rgba(0,0,0,0.06);
  }
  .bottle-label .top-stripe { position: absolute; left: 0; top: 0; width: 100%; height: 14px; }
  .bottle-label .brand-area {
    position: absolute; left: 0; top: 14px; width: 100%; height: 364px;
    display: flex; align-items: center; justify-content: center;
  }
  .bottle-label .product-band { position: absolute; left: 0; bottom: 0; width: 100%; height: 202px; color: var(--text-on-gold); }
  .bottle-label .product-name { position: absolute; left: 0; right: 0; top: 32px; text-align: center; font-size: 30px; letter-spacing: 0.5px; }
  .bottle-label .volume { position: absolute; left: 26px; bottom: 22px; font-size: 25px; line-height: 1.3; }
  .bottle-label .claim { position: absolute; right: 18px; bottom: 22px; font-size: 25px; font-weight: 400; }

  /* Carton front panel, flattened */
  .carton-front {
    position: absolute; left: 640px; top: 90px; width: 430px; height: 880px;
    background: linear-gradient(90deg, var(--paper-shade) 0%, var(--paper) 30%, var(--paper) 75%, var(--paper-shade) 100%);
    box-shadow: 0 2px 10px rgba(0,0,0,0.06);
  }
  .carton-front .brand-area {
    position: absolute; left: 0; top: 190px; width: 100%; height: 240px;
    display: flex; align-items: center; justify-content: center;
  }
  .carton-front .product-band { position: absolute; left: 0; bottom: 0; width: 100%; height: 272px; color: var(--text-on-gold); }
  .carton-front .product-name { position: absolute; left: 28px; top: 78px; font-size: 26px; letter-spacing: 0.5px; }
  .carton-front .claim { position: absolute; right: 28px; bottom: 34px; font-size: 25px; font-weight: 400; }

  .brand-name {
    color: var(--ink-olive);
    text-align: center;
    text-transform: uppercase;
    font-weight: 300;
    line-height: 1.5;
  }
  .bottle-label .brand-name { font-size: 30px; letter-spacing: 9px; }
  .carton-front .brand-name { font-size: 32px; letter-spacing: 10px; }
</style>
</head>
<body>
<main class="canvas">

  <section class="bottle-label" aria-label="Bottle label">
    <div class="top-stripe gold"></div>
    <div class="brand-area">
      <p class="brand-name">Velumi<br>Organics</p>
    </div>
    <div class="product-band gold">
      <h1 class="product-name">LUXE FACIAL OIL</h1>
      <p class="volume">30ml<br>(1.01 oz)</p>
      <p class="claim">100% Natural</p>
    </div>
  </section>

  <section class="carton-front" aria-label="Carton front panel">
    <div class="brand-area">
      <p class="brand-name">Velumi<br>Organics</p>
    </div>
    <div class="product-band gold">
      <h2 class="product-name">LUXE FACIAL OIL</h2>
      <p class="claim">100% Natural</p>
    </div>
  </section>

</main>
</body>
</html>
```